Book Cover for a Short Story called “Salt Orchard"

Pretty Straightforward. Looking for a 5.5X8.5 book cover. The story is a very short (40 pages) story about a man who moves from Greece to Canada in 1920. I have three photos to provide. One is the house that he left in greece. THen I have photos of him and his wife who he met in Toronto. I think I want the house photo on the front...
I will need cover for paper back and e-book. The ISBN numbers are:

ISBN: 978-1-2459083-3-2 (e-book)
ISBN: 978-1-2459083-1-7 (paperback)

If you want you can read it at https://kelvarunde.com/fiction/salt-orchard/

Colors
0094D4
00A9DD
6FCCEA
C7EBF8
E9F6FB

Requirements
Must have
• Room for a blurb about the book on the back cover. ISBN Number

```html
<!DOCTYPE html>
<html lang="en">
<head>
<meta charset="utf-8">
<title>Salt Orchard – Cover Spread</title>
<link href="https://fonts.googleapis.com/css2?family=Cormorant+Garamond:ital,wght@0,500;1,500;1,600&family=Open+Sans:wght@400;700&display=swap" rel="stylesheet">
<style>
  :root {
    --stage: #4a4a4a;
    --paper: #ffffff;
    --gold: #a2842f;
    --ink: #2b2b2b;
    --ink-strong: #111111;
    --photo-light: #dcdcdc;
    --photo-mid: #b9b9b9;
    --photo-dark: #7d7d7d;
  }
  * { box-sizing: border-box; margin: 0; padding: 0; }
  html, body {
    width: 1200px; height: 761px; overflow: hidden;
    background: var(--stage);
  }
  .spread {
    position: absolute; left: 133px; top: 20px;
    width: 933px; height: 720px;
    background: var(--paper);
    display: flex;
  }
  .back-cover { position: relative; width: 470px; height: 100%; }
  .front-cover { position: relative; width: 463px; height: 100%; }

  .back-title {
    position: absolute; left: 0; right: 0; top: 78px;
    text-align: center;
    font-family: "Cormorant Garamond", serif;
    font-style: italic; font-weight: 600;
    font-size: 60px; line-height: 1;
    color: var(--gold);
  }
  .blurb, .author-bio {
    font-family: "Open Sans", sans-serif;
    font-size: 9.6px; line-height: 15px;
    color: var(--ink); text-align: justify;
  }
  .blurb { position: absolute; left: 48px; top: 158px; width: 379px; }
  .author-photo {
    position: absolute; left: 10px; top: 250px; width: 208px; height: 314px;
    background: linear-gradient(180deg, #9aa3b5 0%, #37476e 45%, #2c3b60 70%, rgba(255,255,255,1) 100%);
    border-radius: 90px 90px 0 0;
  }
  .author-bio { position: absolute; left: 219px; top: 262px; width: 208px; }
  .author-bio p + p { margin-top: 15px; }
  .isbn {
    position: absolute; left: 33px; top: 659px;
    font-family: "Open Sans", sans-serif; font-weight: 700;
    font-size: 9.6px; color: var(--ink-strong);
  }

  .cover-photo { position: absolute; left: 0; top: 0; width: 463px; height: 570px; }
  .front-title {
    position: absolute; left: 37px; top: 584px;
    font-family: "Cormorant Garamond", serif;
    font-style: italic; font-weight: 600;
    font-size: 72px; line-height: 1;
    color: var(--gold); white-space: nowrap;
  }
  .front-author {
    position: absolute; right: 72px; top: 660px;
    font-family: "Cormorant Garamond", serif; font-weight: 500;
    font-size: 15px; letter-spacing: 3px;
    color: var(--ink);
  }
</style>
</head>
<body>
  <main class="spread">
    <section class="back-cover">
      <h2 class="back-title">Salt Orchard</h2>
      <p class="blurb">Lorem ipsum dolor sit amet, consectetur adipiscing elit, sed do eiusmod tempor incididunt ut labore et dolore magna aliqua. Quis ipsum suspendisse ultrices gravida. Risus commodo viverra maecenas accumsan lacus vel facilisis. Lorem ipsum dolor sit amet, consectetur adipiscing elit, sed do eiusmod tempor incididunt ut labore et dolore magna aliqua.</p>
      <div class="author-photo" role="img" aria-label="Portrait of the author in a navy blazer, arms crossed, fading into white"></div>
      <div class="author-bio">
        <p>Quis ipsum suspendisse ultrices gravida. Risus commodo viverra maecenas accumsan lacus vel facilisis. Lorem ipsum dolor sit amet, consectetur adipiscing elit, sed do eiusmod tempor incididunt ut labore et dolore magna aliqua. Quis ipsum suspendisse ultrices gravida. Risus commodo viverra maecenas accumsan lacus vel facilisis.</p>
        <p>Quis ipsum suspendisse ultrices gravida. Risus commodo viverra maecenas accumsan lacus vel facilisis. Lorem ipsum dolor sit amet, consectetur adipiscing elit, sed do eiusmod tempor incididunt ut labore et dolore magna aliqua. Quis ipsum suspendisse ultrices gravida. Risus commodo viverra maecenas accumsan lacus vel facilisis.</p>
      </div>
      <p class="isbn">ISBN: 978-1-2459083-1-7</p>
    </section>

    <section class="front-cover">
      <svg class="cover-photo" viewBox="0 0 463 570" role="img" aria-label="Faded archival photographs of a young man and a woman above an old stone house in Greece, with a torn paper edge">
        <defs>
          <linearGradient id="photo-tone" x1="0" y1="0" x2="0" y2="1">
            <stop offset="0" stop-color="var(--photo-light)"/>
            <stop offset="0.55" stop-color="var(--photo-mid)"/>
            <stop offset="1" stop-color="var(--photo-dark)"/>
          </linearGradient>
        </defs>
        <path fill="url(#photo-tone)" d="M0 0 H463 V540 L450 543 L432 538 L410 546 L388 541 L366 549 L340 544 L318 552 L296 548 L270 555 L248 551 L224 558 L200 553 L176 560 L150 555 L128 561 L104 556 L80 552 L58 548 L36 544 L18 546 L0 541 Z"/>
      </svg>
      <h1 class="front-title">Salt Orchard</h1>
      <p class="front-author">KELVA RUNDE</p>
    </section>
  </main>
</body>
</html>
```